Revamp a website that sells books on machine learning and A.I

Hello I would like to create a minimalist concept to revamp this website:

www.quillvane.co.uk

We can change everything including the logo.

Somethings that I don't like:
- Generic images of people.
- Robot images.

The books are about the mathematics for machine learning and A.I and I would like for the website to have a blog as well as a scheduling tool, were people can book a call with me.

The scheduling tool, needs to have text and different tiers, for example 15 m free and 60 m 45 usd

Target Market(s)

university students and mathematics enthusiasts

Industry/Entity Type

machine learning, education, books, mathematics, A.I

Number of Pages Required

4 page

Requirements
Must have
• Landing Page, blog page, scheduling page, optimised conversion funnel
Should not have
• Arbitrary images from people or robots

```html
<!DOCTYPE html>
<html lang="en">
<head>
<meta charset="utf-8">
<title>Quillvane – Mathematics for Machine Learning</title>
<link href="https://fonts.googleapis.com/css2?family=Poppins:wght@400;500;600&family=Nunito+Sans:wght@400;600;700&display=swap" rel="stylesheet">
<style>
:root{
  --red:#d8332a;
  --red-deep:#d2232c;
  --maroon:#7a0e12;
  --yellow:#fbb845;
  --mist:#f3f4f8;
  --white:#ffffff;
  --ink:#111111;
  --green:#23875a;
  --grey:#d9d9d9;
  --cover:#f2c65a;
}
*{box-sizing:border-box;margin:0;padding:0}
html,body{width:1200px;height:3565px;overflow:hidden}
body{position:relative;background:var(--white);font-family:'Nunito Sans',sans-serif;color:var(--ink)}
.abs{position:absolute}
h1,h2,h3,.display{font-family:'Poppins',sans-serif;font-weight:500}
.btn{position:absolute;display:flex;align-items:center;justify-content:center;border-radius:20px;font-family:'Poppins',sans-serif;font-size:15px;color:var(--maroon);background:var(--yellow)}
.btn-outline{background:transparent;border:1.5px solid var(--maroon)}
.cover{position:absolute;background:linear-gradient(160deg,#f5cd62,#e9b443);box-shadow:0 2px 6px rgba(0,0,0,.2)}
.tag{position:absolute;background:var(--yellow);color:var(--maroon);font-family:'Poppins',sans-serif;font-size:15px;display:flex;align-items:center;justify-content:center}

/* nav */
.nav{position:absolute;left:0;top:0;width:1200px;height:69px;background:var(--white)}
.brand{position:absolute;display:flex;align-items:center;gap:6px;font-family:'Poppins',sans-serif;font-weight:600;color:var(--maroon)}
.brand-dot{border-radius:50%;background:var(--yellow)}
.nav-links{position:absolute;left:802px;top:25px;display:flex;gap:18px;font-size:14px;font-family:'Poppins',sans-serif}

/* hero */
.hero{position:absolute;left:0;top:69px;width:1200px;height:606px;background:var(--mist)}
.hero-title{position:absolute;left:50px;top:168px;font-size:34px;line-height:48px;font-weight:500}
.hero-sub{position:absolute;left:50px;top:308px;font-size:17px}
.release-title{position:absolute;color:var(--white);font-family:'Poppins',sans-serif;font-weight:600;font-size:22px;line-height:31px}
.release-text{position:absolute;color:var(--white);font-size:16px;line-height:21px}

/* quote */
.quote{position:absolute;left:0;top:675px;width:1200px;height:243px;background:var(--yellow)}
.quote-text{position:absolute;left:100px;top:52px;font-family:'Poppins',sans-serif;font-weight:600;font-size:30px;line-height:45px;color:var(--maroon)}
.quote-by{position:absolute;left:100px;top:162px;font-family:'Poppins',sans-serif;font-size:20px}

/* books */
.books{position:absolute;left:0;top:918px;width:1200px;height:618px;background:var(--mist)}
.section-title{position:absolute;width:1200px;text-align:center;font-family:'Poppins',sans-serif;font-size:33px;font-weight:500}
.book-desc{position:absolute;color:var(--white);font-size:16px;line-height:21px}

/* about */
.about{position:absolute;left:0;top:1536px;width:1200px;height:678px;background:var(--white)}
.center{position:absolute;width:1200px;text-align:center}

/* consultation */
.consult{position:absolute;left:0;top:2214px;width:1200px;height:674px;background:var(--red-deep);color:var(--white)}
.tier{position:absolute;top:184px;height:89px;border-radius:6px;background:rgba(255,255,255,.14)}
.tier-name{position:absolute;left:6px;top:8px;font-size:10px;font-weight:700}
.tier-min{position:absolute;left:6px;top:28px;font-size:16px;color:var(--yellow)}
.tier-price{position:absolute;right:6px;top:32px;font-size:10px;font-weight:700}
.tier-pick{position:absolute;left:50%;transform:translateX(-50%);top:62px;width:40px;height:17px;border-radius:9px;border:1px solid var(--yellow);font-size:6px;display:flex;align-items:center;justify-content:center}
.field{position:absolute;left:623px;width:348px;border-radius:3px;background:rgba(255,255,255,.1);font-size:13px;padding:9px 15px}

/* updates */
.updates{position:absolute;left:0;top:2888px;width:1200px;height:410px;background:var(--white)}

/* footer */
.footer{position:absolute;left:0;top:3298px;width:1200px;height:267px;background:var(--mist)}
.foot-links{position:absolute;left:591px;top:58px;font-size:13px;line-height:23.5px}
</style>
</head>
<body>

<header class="nav">
  <div class="brand" style="left:64px;top:22px;font-size:16px">
    <span class="brand-dot" style="width:22px;height:22px"></span>Quillvane
  </div>
  <nav class="nav-links"><span>Home</span><span>About</span><span>Books</span><span>Blogs</span></nav>
  <div class="btn" style="left:1031px;top:20px;width:140px;height:30px;font-size:13px;gap:6px">
    <svg width="12" height="12" viewBox="0 0 24 24"><path fill="#7a0e12" d="M6.6 10.8a15 15 0 006.6 6.6l2.2-2.2c.3-.3.7-.4 1-.2 1.1.4 2.3.6 3.6.6.6 0 1 .4 1 1V20c0 .6-.4 1-1 1A17 17 0 013 4c0-.6.4-1 1-1h3.5c.6 0 1 .4 1 1 0 1.3.2 2.5.6 3.6.1.3 0 .7-.2 1z"/></svg>
    Schedule call
  </div>
</header>

<section class="hero">
  <h1 class="hero-title">Master Mathematics for<br>Machine Learning</h1>
  <svg class="abs" style="left:50px;top:265px" width="270" height="20"><path d="M2 14 Q135 -4 268 14" stroke="var(--green)" stroke-width="3" fill="none"/></svg>
  <p class="hero-sub">Transform your understanding with practical, real-world applications.</p>
  <div class="btn" style="left:50px;top:360px;width:113px;height:36px">Shop now</div>
  <div class="btn btn-outline" style="left:180px;top:360px;width:127px;height:36px">Learn more</div>

  <svg class="abs" style="left:0;top:0" width="1200" height="606"><polygon points="541,233 1200,233 1200,537 758,537" fill="var(--red)"/></svg>
  <div class="tag" style="left:541px;top:198px;width:137px;height:33px">Latest Release</div>
  <div class="cover" role="img" aria-label="Book cover: Ahead of the Model, Vol 2 Calculus" style="left:728px;top:163px;width:145px;height:222px"></div>
  <h3 class="release-title" style="left:893px;top:255px">Ahead of the Model<br>Vol 2 - Calculus</h3>
  <div class="btn" style="left:894px;top:331px;width:137px;height:36px">Start reading</div>
  <p class="release-text" style="left:728px;top:401px;width:430px">Calculus is key in machine learning, aiding function analysis and model tuning. Derivatives and integrals optimize neural networks and reduce errors, making calculus essential.</p>
</section>

<section class="quote">
  <p class="quote-text">Embark on a buzzing exploration of calculus in machine learning,<br>where bees are your companions in deciphering the secrets of AI.</p>
  <p class="quote-by">- Tomas Ferreira</p>
</section>

<section class="books">
  <h2 class="section-title" style="top:90px">There are two of them!</h2>
  <svg class="abs" style="left:562px;top:130px" width="76" height="12"><path d="M2 9 Q38 -2 74 9" stroke="var(--green)" stroke-width="3" fill="none"/></svg>
  <svg class="abs" style="left:0;top:0" width="1200" height="618"><polygon points="0,245 482,245 684,598 0,598" fill="var(--red)"/><polygon points="523,245 1200,245 1200,598 739,598" fill="var(--red)"/></svg>

  <div class="cover" role="img" aria-label="Book cover: Ahead of the Model, Vol 2 Calculus" style="left:50px;top:189px;width:155px;height:236px"></div>
  <div class="tag" style="left:327px;top:245px;width:135px;height:33px">Latest Release</div>
  <h3 class="release-title" style="left:230px;top:310px">Ahead of the Model<br>Vol 2 - Calculus</h3>
  <p class="book-desc" style="left:50px;top:441px;width:330px">Master Calculus concepts essential for advanced machine learning techniques.</p>
  <div class="btn" style="left:50px;top:505px;width:126px;height:34px">Add to Cart</div>

  <div class="cover" role="img" aria-label="Book cover: Ahead of the Model, Vol 1 Linear Algebra" style="left:734px;top:189px;width:155px;height:236px"></div>
  <h3 class="release-title" style="left:913px;top:310px">Ahead of the Model<br>Vol 1 - Linear Algebra</h3>
  <p class="book-desc" style="left:734px;top:441px;width:400px">Understand the core principles of Linear Algebra and their applications in AI.</p>
  <div class="btn" style="left:734px;top:505px;width:126px;height:34px">Add to Cart</div>
</section>

<section class="about">
  <h2 class="section-title" style="top:56px">About me</h2>
  <svg class="abs" style="left:542px;top:100px" width="140" height="12"><path d="M2 9 Q70 -3 138 9" stroke="var(--green)" stroke-width="3" fill="none"/></svg>
  <div class="abs" role="img" aria-label="Portrait of the author" style="left:528px;top:143px;width:144px;height:144px;border-radius:50%;background:var(--grey)"></div>
  <h3 class="center display" style="top:319px;font-size:23px;color:var(--maroon)">Tomas Ferreira</h3>
  <p class="center display" style="top:365px;font-size:17px;color:var(--maroon);font-weight:400">A Mathematician and now a book writer</p>
  <p class="abs" style="left:240px;top:408px;width:720px;text-align:center;font-size:15.5px;line-height:21px">I am a mathematician with over a decade of experience in developing and deploying machine learning systems. My books are written in an conversational style with humour. They are rich in practical applications, enabling readers to not only grasp the concepts but also understand their real-world applications in the field of Data Science.</p>
  <div class="abs" style="left:586px;top:520px;width:28px;height:28px;border-radius:50%;background:var(--yellow)"></div>
  <div class="btn btn-outline" style="left:497px;top:579px;width:205px;height:37px">Know more about me</div>
</section>

<section class="consult">
  <h2 class="abs display" style="left:86px;top:153px;font-size:35px">Book a Consultation</h2>
  <svg class="abs" style="left:86px;top:198px" width="272" height="18"><path d="M2 14 Q136 -6 270 14" stroke="var(--yellow)" stroke-width="3" fill="none"/></svg>
  <p class="abs" style="left:86px;top:262px;font-size:18px;line-height:24px">Schedule your call and get expert advice on<br>your mathematical journey.</p>
  <p class="abs" style="left:86px;top:328px;font-size:16px;font-weight:700">- Tomas Ferreira</p>

  <svg class="abs" style="left:598px;top:66px" width="165" height="72">
    <polygon points="16,14 28,24 18,28" fill="var(--yellow)"/>
    <polygon points="25,6 160,6 160,32 25,32" fill="var(--yellow)"/>
    <polygon points="25,32 92,32 92,58 40,58 32,72 30,58 25,58" fill="#f29a18"/>
    <polygon points="98,40 126,44 112,52" fill="var(--yellow)"/>
  </svg>
  <p class="abs display" style="left:629px;top:73px;font-size:16px;font-weight:600;color:var(--red-deep);line-height:26px">FRIST 15 MIN<br>FREE</p>
  <p class="abs" style="left:623px;top:150px;font-size:15px;font-weight:700">Select Plans :</p>

  <div class="tier" style="left:623px;width:88px">
    <span class="tier-name">Tier 1</span><span class="tier-min">15 Min</span><span class="tier-price">Free</span>
    <span class="tier-pick" style="background:var(--yellow);color:var(--maroon)">Selected</span>
  </div>
  <div class="tier" style="left:724px;width:105px">
    <span class="tier-name">Tier 2</span><span class="tier-min">60 Min</span><span class="tier-price">45 USD</span>
    <span class="tier-pick">Select</span>
  </div>
  <div class="tier" style="left:844px;width:111px">
    <span class="tier-name">Tier 2</span><span class="tier-min">120 Min</span><span class="tier-price">90 USD</span>
    <span class="tier-pick">Select</span>
  </div>
  <p class="abs" style="left:623px;top:288px;font-size:10px;display:flex;gap:8px;align-items:center">
    <svg width="12" height="12" viewBox="0 0 12 12"><circle cx="6" cy="6" r="5" stroke="#fff" fill="none"/><path d="M6 5v4M6 3v1" stroke="#fff"/></svg>
    You are eligible for a complimentary 15-minute consultation call.
  </p>
  <div class="field" style="top:320px;height:35px">Name</div>
  <div class="field" style="top:373px;height:34px">Email</div>
  <div class="field" style="top:424px;height:131px">Message</div>
  <div class="btn" style="left:623px;top:587px;width:122px;height:33px">Book Now !</div>
</section>

<section class="updates">
  <svg class="abs" style="left:0;top:0" width="1200" height="410">
    <polygon points="0,13 257,13 0,274" fill="var(--red)"/>
    <rect x="174" y="57" width="850" height="298" fill="var(--mist)"/>
    <polygon points="1200,136 1200,394 947,394" fill="var(--yellow)"/>
  </svg>
  <h2 class="center display" style="top:105px;font-size:37px;color:var(--maroon)">Unlock Latest Updates !</h2>
  <p class="center" style="top:170px;font-size:13px">Subscribe to receive a free chapter and updates.</p>
  <div class="abs" style="left:425px;top:230px;width:350px;height:35px;border-radius:18px;background:#e4e5ea;font-size:11px;padding:10px 16px;color:#555">Email</div>
  <div class="btn" style="left:673px;top:230px;width:102px;height:35px;font-size:14px">Subscribe</div>
</section>

<footer class="footer">
  <div class="brand" style="left:218px;top:80px;font-size:24px">
    <span class="brand-dot" style="width:30px;height:30px"></span>Quillvane
  </div>
  <p class="abs display" style="left:164px;top:171px;font-size:13px;color:var(--maroon)">Transform Your Mathematical Skills</p>
  <div class="foot-links"><div>Home</div><div>About</div><div>Blog</div><div>Books</div><div>Code And Exercises</div></div>
  <p class="abs" style="left:932px;top:58px;font-size:13px">Follow Us On</p>
  <div class="abs" style="left:926px;top:89px;display:flex;gap:12px">
    <span style="width:12px;height:12px;border-radius:50%;background:#333"></span>
    <span style="width:12px;height:12px;border-radius:50%;background:#333"></span>
    <span style="width:12px;height:12px;border-radius:50%;background:#333"></span>
    <span style="width:12px;height:12px;border-radius:50%;background:#333"></span>
  </div>
  <div class="btn" style="left:870px;top:132px;width:198px;height:34px;gap:6px">
    <svg width="13" height="13" viewBox="0 0 24 24"><path fill="#7a0e12" d="M6.6 10.8a15 15 0 006.6 6.6l2.2-2.2c.3-.3.7-.4 1-.2 1.1.4 2.3.6 3.6.6.6 0 1 .4 1 1V20c0 .6-.4 1-1 1A17 17 0 013 4c0-.6.4-1 1-1h3.5c.6 0 1 .4 1 1 0 1.3.2 2.5.6 3.6.1.3 0 .7-.2 1z"/></svg>
    Schedule a call now !
  </div>
  <div class="abs" style="left:50px;top:217px;width:1100px;height:1px;background:#bbb"></div>
  <p class="center" style="top:239px;font-size:8px">© 2023 Quillvane. All Rights Reserved.</p>
</footer>

</body>
</html>
```